Electrical contractor Brochure design

We are looking a elegant brochure design for our new branding campaign. Logo ai file is attached. We mainly work in power plants and manufacturing facilities. We would like some pictures to show those types of facilities.

Target Market(s)

Industrial commercial electrician

Industry/Entity Type

Contractor

Font styles to use
Sans Serif

```html
<!DOCTYPE html>
<html lang="en">
<head>
<meta charset="utf-8">
<title>Voltline Electric – Brochure</title>
<link href="https://fonts.googleapis.com/css2?family=Exo+2:wght@400;600;700&family=Open+Sans:wght@600;700&display=swap" rel="stylesheet">
<style>
:root{
  --red:#c4161c;
  --dark:#1e1e20;
  --ink:#2a2a2e;
  --paper:#eef0f5;
  --bg:#dcdde0;
  --white:#ffffff;
}
*{box-sizing:border-box;margin:0;padding:0}
html,body{width:1200px;height:789px;overflow:hidden;background:var(--bg)}
body{font-family:"Exo 2",sans-serif;color:var(--ink)}
.spread{position:absolute;left:80px;top:26px;width:1040px;height:736px;background:var(--paper);box-shadow:0 4px 18px rgba(0,0,0,.18)}
.fold{position:absolute;left:519px;top:0;width:2px;height:100%;background:linear-gradient(90deg,rgba(0,0,0,.08),rgba(255,255,255,.4));z-index:5}
.bands{position:absolute;inset:0;z-index:1}
.photo{position:absolute;z-index:2}
.photo-plant{left:300px;top:125px;width:680px;height:330px;
  background:linear-gradient(180deg,#9fb4cc 0%,#8397ae 35%,#56606c 65%,#2f3640 100%)}
.photo-assembly{left:40px;top:215px;width:310px;height:230px;z-index:3;
  background:linear-gradient(135deg,#b9bcc0 0%,#7d7f7a 45%,#c9b43a 70%,#5c5e62 100%)}
.intro{position:absolute;left:40px;top:48px;width:300px;font-size:9px;line-height:1.35;color:var(--ink);z-index:3}
.contact{position:absolute;left:40px;top:520px;z-index:3}
.contact h2{font-size:17px;font-weight:400;letter-spacing:.5px;color:var(--ink)}
.contact h2 span{color:var(--red);font-weight:600}
.contact .rule{width:80px;height:2px;background:var(--red);margin:6px 0 10px}
.contact p{display:flex;align-items:flex-start;gap:8px;font-size:13px;line-height:1.3;margin-bottom:8px}
.contact svg{flex:none;margin-top:2px}
.brand{position:absolute;z-index:3;display:flex;align-items:center;gap:8px;
  font-family:"Exo 2",sans-serif;font-weight:700;font-size:22px;color:var(--dark);white-space:nowrap}
.brand .mark{width:26px;height:26px;border-radius:50%;background:var(--red)}
.brand-back{left:340px;top:545px}
.brand-front{right:36px;top:50px}
.social{position:absolute;left:410px;top:684px;display:flex;gap:8px;z-index:3}
.social span{width:20px;height:20px;border-radius:50%;background:#2f7fc1}
.url{position:absolute;z-index:3;color:var(--white);font-size:15px;white-space:nowrap}
.url b{font-weight:700}
.url-back{left:40px;top:704px;display:flex;align-items:center;gap:8px}
.url-front{right:34px;top:700px}
.headline{position:absolute;right:38px;top:472px;text-align:right;z-index:3}
.headline .l1{font-family:"Open Sans",sans-serif;font-weight:700;font-size:22px;color:var(--red)}
.headline .l2{font-family:"Open Sans",sans-serif;font-weight:600;font-size:20px;color:var(--ink);margin-top:2px}
.call{position:absolute;left:560px;top:700px;z-index:3;font-family:"Open Sans",sans-serif;font-weight:700;font-size:14px;color:var(--white);letter-spacing:.3px}
</style>
</head>
<body>
<main class="spread">
  <svg class="bands" width="1040" height="736" viewBox="0 0 1040 736" aria-hidden="true">
    <!-- back cover top edge -->
    <polygon points="0,0 330,0 322,7 0,7" fill="var(--red)"/>
    <polygon points="330,0 520,0 520,3 327,3" fill="var(--dark)"/>
    <!-- front cover top edge -->
    <polygon points="760,0 1040,0 1040,6 752,6" fill="var(--red)"/>
    <!-- red accent above plant photo -->
    <polygon points="520,105 780,105 770,125 520,125" fill="var(--red)"/>
    <polygon points="440,118 520,118 520,132 432,132" fill="var(--red)"/>
    <!-- red accent below plant photo -->
    <polygon points="700,455 980,455 960,478 680,478" fill="var(--red)"/>
    <!-- back cover bottom bands -->
    <polygon points="372,650 520,650 520,736 336,736" fill="var(--dark)"/>
    <polygon points="0,688 400,688 370,736 0,736" fill="var(--red)"/>
    <!-- front cover bottom bands -->
    <polygon points="520,680 860,680 840,736 520,736" fill="var(--dark)"/>
    <polygon points="870,655 1040,655 1040,736 840,736" fill="var(--red)"/>
  </svg>

  <div class="fold"></div>

  <!-- back cover -->
  <p class="intro">Lorem ipsum dolor sit amet, consectetur adipiscing elit, sed do eiusmod tempor incididunt ut labore et dolore magna aliqua. Ut enim ad minim veniam, quis nostrud exercitation ullamco laboris nisi ut aliquip ex ea commodo consequat. Duis aute irure dolor in reprehenderit in voluptate velit esse cillum dolore eu fugiat nulla pariatur. Excepteur sint occaecat cupidatat non proident, sunt in culpa qui officia deserunt mollit anim id est laborum.</p>

  <div class="photo photo-plant" role="img" aria-label="Power plant with silos and towers lit at dusk by the sea"></div>
  <div class="photo photo-assembly" role="img" aria-label="Manufacturing line with machinery and a worker"></div>

  <section class="contact">
    <h2>CONTACT <span>DETAILS</span></h2>
    <div class="rule"></div>
    <p>
      <svg width="12" height="14" viewBox="0 0 12 14" aria-hidden="true"><path d="M6 1a4 4 0 0 1 4 4c0 3-4 8-4 8S2 8 2 5a4 4 0 0 1 4-4z" fill="none" stroke="var(--red)" stroke-width="1.6"/><circle cx="6" cy="5" r="1.4" fill="var(--red)"/></svg>
      <span>Address line 1<br>Address line 2, Address line 2</span>
    </p>
    <p>
      <svg width="13" height="13" viewBox="0 0 13 13" aria-hidden="true"><circle cx="6.5" cy="6.5" r="5.5" fill="none" stroke="var(--red)" stroke-width="1.4"/><path d="M4.5 4c.5 2 1.8 3.6 4 4.5l.6-1" fill="none" stroke="var(--red)" stroke-width="1.4"/></svg>
      <span>0123 456 789</span>
    </p>
    <p>
      <svg width="13" height="10" viewBox="0 0 13 10" aria-hidden="true"><rect x="1" y="1" width="11" height="8" fill="none" stroke="var(--red)" stroke-width="1.3"/><path d="M1 1l5.5 4.5L12 1" fill="none" stroke="var(--red)" stroke-width="1.3"/></svg>
      <span>info@yourwebsite.com</span>
    </p>
  </section>

  <div class="brand brand-back"><span class="mark"></span>Voltline Electric</div>

  <div class="social" aria-hidden="true"><span></span><span></span><span></span></div>

  <div class="url url-back">
    <svg width="14" height="14" viewBox="0 0 14 14" aria-hidden="true"><circle cx="7" cy="7" r="6" fill="none" stroke="#fff" stroke-width="1.3"/><ellipse cx="7" cy="7" rx="2.6" ry="6" fill="none" stroke="#fff" stroke-width="1.1"/><path d="M1 7h12" stroke="#fff" stroke-width="1.1"/></svg>
    <span>www.<b>yourwebsite</b>.com</span>
  </div>

  <!-- front cover -->
  <div class="brand brand-front"><span class="mark"></span>Voltline Electric</div>

  <div class="headline">
    <div class="l1">LOREM IPSUM DOLOR SIT AMET</div>
    <div class="l2">CONSECTETUR ADIPISCING</div>
  </div>

  <div class="call">CALL US NOW - 0123 456 789</div>
  <div class="url url-front">www.<b>yourweb</b>.com</div>
</main>
</body>
</html>
```